Custom Home Builder Website

We need a re-design of a website for our client: "http://www.tovarelbuilds.com". Their current design is outdated and has flash. We need to make it responsive for all devices and with a more professional look.

Pages to consider:
1. Home page
2. Portfolio page - gallery of projects (multiple images of a project with captions, and a main text area for each project).

Good clean design reflecting quality craftsmanship is a must.

We only need designs, no coding required

Target Market(s)

The intended market is home owners looking to build with a reputable and professional home builder.

Industry/Entity Type

Home Builder

Requirements
Must have
• Must Have:
• - main areas of site: home, portfolio, video gallery, contact
Nice to have
• - Maybe pullquotes from testimonials placed as slideshow?

```html
<!DOCTYPE html>
<html lang="en">
<head>
<meta charset="utf-8">
<title>Tovarel Built – Custom Home Builder</title>
<link href="https://fonts.googleapis.com/css2?family=Open+Sans:wght@400;600;700&display=swap" rel="stylesheet">
<style>
:root{
  --gold:#c0894a;
  --gold-light:#d2a36c;
  --band:#c8965c;
  --ink:#333333;
  --text:#666666;
  --muted:#8a8a8a;
  --nav:#2f2f2f;
  --footer:#262626;
  --page:#ffffff;
  --soft:#f3f3f3;
}
*{margin:0;padding:0;box-sizing:border-box}
html,body{width:809px;height:1200px;overflow:hidden}
body{font-family:"Open Sans",Arial,sans-serif;background:var(--page);color:var(--text);position:relative}

.site-header{height:80px;position:relative;background:#fff}
.brand{position:absolute;left:104px;top:14px;display:flex;align-items:center;gap:10px}
.brand-mark{width:12px;height:12px;background:var(--gold)}
.brand-name{font-weight:600;color:var(--gold);font-size:24px;letter-spacing:3px;line-height:1}
.call{position:absolute;right:118px;top:22px;display:flex;align-items:center;gap:10px}
.call svg{width:22px;height:30px}
.call-label{font-size:9px;color:var(--muted);letter-spacing:1px}
.call-number{font-size:16px;font-weight:700;color:var(--ink)}

.main-nav{height:23px;background:var(--nav);display:flex;justify-content:center}
.main-nav a{color:#e8e8e8;font-size:9.5px;font-weight:600;text-decoration:none;padding:0 14px;line-height:23px;letter-spacing:.3px}
.main-nav a.active{background:var(--gold)}

.hero{height:297px;background:linear-gradient(180deg,#d8c6a8 0%,#b99a74 35%,#8c6a4a 65%,#c9b392 100%)}

.section-title{display:flex;align-items:center;justify-content:center;gap:16px;color:var(--gold);font-size:19px;font-weight:600;letter-spacing:1px;text-transform:uppercase}
.section-title::before,.section-title::after{content:"";width:60px;height:2px;background:var(--gold)}

.welcome{padding:16px 104px 0}
.welcome p{margin-top:12px;font-size:9px;line-height:15px;text-align:center;color:var(--muted)}

.services{margin-top:26px}
.service-grid{display:flex;justify-content:center;gap:10px;margin-top:16px}
.service{width:143px;height:104px;position:relative}
.service .label{position:absolute;left:0;right:0;bottom:0;height:22px;background:rgba(30,30,30,.85);color:#fff;font-size:11px;font-weight:700;padding-left:8px;line-height:22px}
.s1{background:linear-gradient(135deg,#b9a88c,#6f5e4a)}
.s2{background:linear-gradient(135deg,#9eb3c4,#5d6f7d)}
.s3{background:linear-gradient(135deg,#a9c0d2,#7b6a58)}
.s4{background:linear-gradient(135deg,#d2c0a2,#8a7056)}

.news{position:absolute;top:715px;left:0;width:809px;height:270px;background:var(--band)}
.news-photo{position:absolute;left:104px;top:26px;width:300px;height:228px;background:linear-gradient(180deg,#a7b9c6 0%,#8f7a5e 55%,#5d6b3e 100%)}
.news-photo .label{position:absolute;left:0;right:0;bottom:0;height:30px;background:rgba(25,25,25,.85);color:#fff;font-size:14px;font-weight:700;padding-left:10px;line-height:30px}
.news-photo .arrow{position:absolute;right:10px;top:7px;width:16px;height:16px;border-radius:50%;background:#fff}
.news-body{position:absolute;left:436px;top:28px;width:270px;color:#fff}
.news-body h2{font-size:17px;font-weight:700;color:#fff}
.news-body h3{margin-top:10px;font-size:9px;font-weight:700;letter-spacing:.3px}
.news-body .date{font-size:8px;opacity:.85;margin-top:2px}
.news-body p{margin-top:8px;font-size:8.5px;line-height:13px}
.read-more{display:inline-block;margin-top:20px;border:1px solid #fff;color:#fff;font-size:8px;font-weight:600;padding:5px 14px;letter-spacing:.5px}

.contact{position:absolute;top:1013px;left:0;width:809px}
.contact-inner{display:flex;margin:18px 104px 0}
.map{width:300px;height:108px;background:linear-gradient(135deg,#e6e8dc,#cfd8c4 50%,#e8e3d6)}
.details{margin-left:32px;width:270px}
.details p{font-size:9px;line-height:13px;color:var(--ink)}
.detail-row{display:flex;align-items:center;gap:10px;margin-top:10px;font-size:9px;color:var(--ink)}
.detail-row svg{width:14px;height:14px;flex:none}

.site-footer{position:absolute;left:0;bottom:0;width:809px;height:22px;background:var(--footer);color:#bbb;font-size:8px;text-align:center;line-height:22px}
</style>
</head>
<body>

<header class="site-header">
  <div class="brand"><span class="brand-mark"></span><span class="brand-name">TOVAREL BUILT</span></div>
  <div class="call">
    <svg viewBox="0 0 22 30"><rect x="3" y="1" width="16" height="28" rx="3" fill="#333"/><rect x="6" y="5" width="10" height="17" fill="#fff"/><circle cx="11" cy="25.5" r="1.6" fill="#fff"/></svg>
    <div><div class="call-label">CALL US ON</div><div class="call-number">(503) 555-0148</div></div>
  </div>
</header>

<nav class="main-nav">
  <a href="#">HOME</a><a href="#" class="active">ABOUT US</a><a href="#">SERVICES</a><a href="#">PORTFOLIO</a><a href="#">VIDEO GALLERY</a><a href="#">TOVAREL REWARDS</a><a href="#">NEWS</a><a href="#">CONTACT</a>
</nav>

<div class="hero" role="img" aria-label="Photograph of a bright custom home living room with sectional sofa, kitchen and large windows"></div>

<section class="welcome">
  <h1 class="section-title">Welcome to Tovarel Built</h1>
  <p>Tovarel Custom Homes is a custom home builder and remodeler based in Portland, Oregon, serving the greater Portland metro area and Central Oregon. Whether you need a new kitchen or bathroom, a new addition, or you're ready to build your custom dream home, we make the process simple and stress-free. With a focus on quality, integrity, sustainability and exceptional project management, our goal is to work with you every step of the way to bring your dream to reality.</p>
</section>

<section class="services">
  <h2 class="section-title">Our Services</h2>
  <div class="service-grid">
    <div class="service s1" role="img" aria-label="Residential home photo"><span class="label">Residential</span></div>
    <div class="service s2" role="img" aria-label="Commercial building photo"><span class="label">Commercial</span></div>
    <div class="service s3" role="img" aria-label="New home exterior photo"><span class="label">New Homes</span></div>
    <div class="service s4" role="img" aria-label="Kitchen interior photo"><span class="label">Kitchens</span></div>
  </div>
</section>

<section class="news">
  <div class="news-photo" role="img" aria-label="Photo of a recent home project with autumn trees">
    <span class="label">Recent Projects</span>
    <svg class="arrow" viewBox="0 0 16 16"><circle cx="8" cy="8" r="8" fill="#fff"/><path d="M6.5 4.5 10 8l-3.5 3.5" stroke="#333" stroke-width="1.6" fill="none"/></svg>
  </div>
  <div class="news-body">
    <h2>Tovarel News</h2>
    <h3>LOREM IPSUM DOLOR SIT AMET CONSECTETUR</h3>
    <div class="date">August 12, 2013</div>
    <p>Lorem ipsum dolor sit amet, consectetur adipiscing elit. Donec id ante nibh. Mauris quis nunc nec tellus mollis rutrum. Sed vitae ligula nec nibh tempor porta. Nulla facilisi. Integer congue lorem ut sem fermentum, in posuere lectus dapibus. Phasellus tincidunt lacus at faucibus mollis.</p>
    <span class="read-more">READ MORE</span>
  </div>
</section>

<section class="contact">
  <h2 class="section-title">Contact Us</h2>
  <div class="contact-inner">
    <div class="map" role="img" aria-label="Street map showing the office location"></div>
    <div class="details">
      <p>Lorem ipsum dolor sit amet, consectetur adipiscing elit. Donec id ante nibh. Mauris quis nunc nec tellus mollis rutrum.</p>
      <div class="detail-row"><svg viewBox="0 0 14 14"><path d="M1 6.5 7 1.5l6 5V13H1z" fill="#555"/></svg>4870 NW Alder Ridge Rd, # 210, Hillsboro, OR 97124</div>
      <div class="detail-row"><svg viewBox="0 0 14 14"><rect x="3" y="0.5" width="8" height="13" rx="1.5" fill="#555"/><rect x="4.5" y="2.5" width="5" height="7.5" fill="#fff"/></svg>(503) 555-0148</div>
      <div class="detail-row"><svg viewBox="0 0 14 14"><rect x="0.5" y="2.5" width="13" height="9" fill="#555"/><path d="M1 3l6 5 6-5" stroke="#fff" fill="none"/></svg>info@tovarelbuilds.com</div>
    </div>
  </div>
</section>

<footer class="site-footer">Copyright © 2013 Tovarel Custom Homes. All Rights Reserved</footer>

</body>
</html>
```